Custom Made Digital Jukebox sales and rental website

I need a design for a Custom Made Digital Jukebox sales and rental services website. Domain name is brellatune.com. Exisiting customer shall have a section to register, login/logout, my account, support. All other visitor shall have at least the following options or menu avaialble: Home, FAQ, Services, Products, and Contact us. I have attached a high level requirements pdf file. Please don't be limited by high level requirements file attached, your idea may be better than what I specified. My products are designed base on customer requirements. Common parts are: Bill and Coin Acceptors, Touchscreen or keypad. All of them are wall mount.

Target Market(s)

Custom made digital Jukebox for Home and Commercial use

Industry/Entity Type

Digital

Number of Pages Required

1 page

Requirements
Must have
• PSD required.
Nice to have
• HTML code and CSS Stylesheet
• Logo for BrellaTune
• Inner Pages
Should not have
• Copyright material from related websites, previously developed or any other.

```html
<!DOCTYPE html>
<html lang="en">
<head>
<meta charset="utf-8">
<title>BrellaTune – Custom Made Digital Jukeboxes</title>
<link href="https://fonts.googleapis.com/css2?family=Raleway:wght@300;400;500;600;700;800&display=swap" rel="stylesheet">
<style>
:root{
  --orange:#e8692a;
  --orange-dark:#cf5618;
  --navy:#0c3356;
  --navy-deep:#082744;
  --hero-top:#0a3766;
  --hero-bottom:#1f63a3;
  --tile-dark:#3b3f45;
  --ink:#3a3a3a;
  --muted:#8a8a8a;
  --line:#e2e2e2;
  --page:#f1f1f1;
  --footer:#222427;
  --footer-bar:#17181a;
  --white:#ffffff;
}
*{box-sizing:border-box;margin:0;padding:0}
html,body{width:1200px;height:2400px;overflow:hidden}
body{font-family:'Raleway',Arial,sans-serif;color:var(--ink);background:var(--white);position:relative}
.wrap{width:746px;margin:0 auto;position:relative}

/* header */
.site-header{height:58px;background:var(--white);border-bottom:1px solid var(--line)}
.site-header .wrap{display:flex;align-items:center;height:58px}
.brand{font-weight:800;font-size:22px;color:var(--orange);letter-spacing:.5px;width:220px}
.main-nav{display:flex;gap:0;margin-left:10px}
.main-nav a{font-size:10.5px;font-weight:700;color:#444;text-decoration:none;padding:0 13px;border-right:1px solid #ccc;line-height:12px}
.main-nav a:last-child{border-right:0}
.social-top{margin-left:auto;display:flex;gap:5px}
.social-top span{width:17px;height:17px;background:var(--orange);display:block}

/* hero */
.hero{height:417px;position:relative;overflow:hidden;background:linear-gradient(180deg,var(--hero-top),var(--hero-bottom) 75%,#0d2f55)}
.hero-skyline{position:absolute;left:0;right:0;bottom:0;height:135px;background:linear-gradient(180deg,rgba(5,18,35,.0),#06121f 45%,#040c16)}
.hero-figure{position:absolute;left:827px;top:0;width:320px;height:417px;background:radial-gradient(ellipse at 50% 40%,rgba(240,200,150,.55),rgba(30,30,40,.55) 60%,rgba(0,0,0,0) 75%)}
.hero-copy{position:absolute;left:227px;top:100px;color:var(--white)}
.hero-copy .kicker{font-weight:300;font-size:22px;letter-spacing:1px}
.hero-copy h1{font-weight:800;font-size:46px;line-height:1;margin-top:6px;letter-spacing:.5px}
.hero-copy h1 em{font-style:normal;color:var(--orange)}

/* about */
.about{height:405px;background:var(--page);padding-top:26px}
.about .wrap{display:flex;height:374px}
.about-intro{width:373px;background:var(--orange);color:var(--white);padding:24px 30px;text-align:center}
.about-intro h2{font-size:30px;font-weight:600;margin-bottom:18px}
.about-intro p{font-size:11.5px;line-height:1.45;margin-bottom:10px}
.tiles{display:grid;grid-template-columns:186px 187px;grid-template-rows:187px 187px}
.tile{display:flex;flex-direction:column;align-items:center;justify-content:center;text-align:center;font-weight:800;font-size:14px;line-height:1.2;text-transform:uppercase}
.tile svg{margin-bottom:16px}
.tile.light{background:var(--white);color:#555}
.tile.dark{background:var(--tile-dark);color:var(--white)}
.tile.enquiry{background:var(--white);justify-content:flex-start;padding-top:22px;color:var(--ink)}
.tile.enquiry small{display:block;font-size:10px;font-weight:700;margin-top:10px}
.tile.enquiry .value{font-size:13px;font-weight:500;text-transform:none}
.tile.enquiry.dark-fill{background:var(--tile-dark);color:var(--white)}

/* featured */
.featured{height:427px;background:var(--page);border-top:1px solid var(--line)}
.section-title{text-align:center;font-size:24px;font-weight:300;letter-spacing:1px;color:#666;position:relative}
.section-title b{font-weight:800;color:#444}
.section-title.lined::before,.section-title.lined::after{content:"";position:absolute;top:50%;width:160px;height:1px;background:#cfcfcf}
.section-title.lined::before{left:0}
.section-title.lined::after{right:0}
.featured .section-title{padding-top:67px;text-transform:uppercase}
.products{display:flex;gap:19px;margin-top:40px}
.product{width:173px;background:var(--white);height:262px;text-align:center}
.product-shot{height:133px;background:linear-gradient(180deg,#e8e8e8,#d6d6d6);display:flex;align-items:center;justify-content:center}
.product-shot span{display:block;width:56px;height:100px;background:linear-gradient(180deg,#2a2a2a,#141414);border-radius:3px}
.product h3{font-size:11px;font-weight:800;color:#555;margin:16px 0 10px;text-transform:uppercase}
.product p{font-size:10px;line-height:1.5;color:var(--muted);padding:0 20px}

/* best of */
.best{height:453px;background:var(--navy);color:var(--white)}
.best .section-title{color:var(--white);padding-top:52px;text-transform:uppercase}
.best .section-title b{color:var(--white)}
.best .section-title.lined::before,.best .section-title.lined::after{background:rgba(255,255,255,.35)}
.best-cols{display:flex;gap:8px;margin-top:26px;height:307px}
.best-col{padding:22px 18px}
.best-col h3{font-size:15px;font-weight:800;line-height:1.2;text-transform:uppercase;margin-bottom:12px}
.feature-list{width:240px;background:var(--navy-deep)}
.feature-list ul{list-style:none}
.feature-list li{font-size:10.5px;line-height:1.3;margin-bottom:7px;padding-left:12px;position:relative}
.feature-list li::before{content:"›";position:absolute;left:0;top:-2px;color:var(--orange);font-weight:800;font-size:13px}
.custom-sale{width:250px;background:#eef0f2;color:#555;text-align:center}
.custom-sale h3{color:var(--navy)}
.custom-sale p{font-size:10px;line-height:1.5;margin-bottom:10px;text-align:left}
.rental{width:240px;background:var(--navy-deep)}
.rental p{font-size:10.5px;line-height:1.5;margin-bottom:12px;color:#dbe4ee}
.rental .check{color:var(--orange);font-size:10px;font-weight:800;text-transform:uppercase}
.rental .choose{font-size:10.5px;margin:4px 0 8px}
.date-row{display:flex;gap:6px;margin-bottom:10px}
.date-row span{flex:1;height:22px;background:var(--white);color:#777;font-size:9.5px;padding:5px 6px;position:relative}
.date-row span::after{content:"";position:absolute;right:6px;top:9px;border:4px solid transparent;border-top-color:#888}
.btn{display:inline-block;background:var(--orange);color:var(--white);font-weight:700;font-size:11px;text-transform:uppercase;border:0}
.rental .btn{width:100%;text-align:center;padding:7px 0}

/* contact */
.contact{height:453px;position:relative;background:#eceae6}
.contact-map{position:absolute;inset:0;background:linear-gradient(135deg,#f0eee9,#e2e0db 50%,#ecebe6)}
.contact .wrap{z-index:1}
.contact h2{text-align:center;font-size:34px;font-weight:800;color:#3a3a3a;padding-top:28px}
.contact .lead{text-align:center;font-size:16px;color:#666;margin-top:6px}
.info-boxes{display:flex;gap:8px;margin-top:40px}
.info-box{flex:1;background:var(--white);height:93px;text-align:center;padding-top:26px;position:relative}
.info-box .badge{position:absolute;left:50%;top:-16px;margin-left:-17px;width:34px;height:34px;border-radius:50%;background:var(--orange);display:flex;align-items:center;justify-content:center}
.info-box h4{font-size:14px;font-weight:700;color:#444;text-transform:uppercase}
.info-box p{font-size:10px;color:#777;margin-top:6px;line-height:1.4}
.info-box a{color:var(--orange);text-decoration:none}
.contact-form{margin-top:32px}
.form-row{display:flex;gap:8px}
.field{flex:1;height:27px;background:var(--white);border:1px solid #ddd;font-size:10px;color:#999;padding:7px 8px}
.field.message{height:61px;margin-top:13px;width:100%}
.form-foot{display:flex;justify-content:space-between;align-items:center;margin-top:14px}
.form-foot .btn{padding:6px 18px}
.form-foot small{font-size:10px;color:#666}

/* footer */
.site-footer{height:155px;background:var(--footer);color:#999}
.footer-cols{display:flex;padding-top:38px}
.footer-col{width:192px}
.footer-col h5{font-size:11px;font-weight:600;color:#aaa;text-transform:uppercase;letter-spacing:.5px;margin-bottom:9px}
.footer-col li{list-style:none;font-size:9.5px;line-height:1.6;color:#888}
.footer-col li::before{content:"› ";color:#666}
.footer-bar{height:32px;background:var(--footer-bar)}
.footer-bar .wrap{display:flex;align-items:center;height:32px;font-size:9.5px;color:#777}
.footer-social{margin-left:auto;display:flex;gap:10px}
.footer-social span{width:12px;height:12px;border-radius:50%;background:#4a6a8a;display:block}
</style>
</head>
<body>

<header class="site-header">
  <div class="wrap">
    <div class="brand">BrellaTune</div>
    <nav class="main-nav">
      <a>HOME</a><a>SERVICES</a><a>PRODUCTS</a><a>JUKEBOXES</a><a>FAQ</a><a>CONTACT US</a>
    </nav>
    <div class="social-top"><span></span><span></span></div>
  </div>
</header>

<section class="hero">
  <div class="hero-skyline" role="img" aria-label="Night city skyline silhouette"></div>
  <div class="hero-figure" role="img" aria-label="Illustrated woman wearing headphones enjoying music"></div>
  <div class="hero-copy">
    <div class="kicker">DISCOVER THE POWER OF</div>
    <h1><em>BRELLA</em>TUNE</h1>
  </div>
</section>

<section class="about">
  <div class="wrap">
    <div class="about-intro">
      <h2>What we do?</h2>
      <p>Long gone are the days of attending events hoping that the DJ would remember to play your favorite songs. Hear the music you love, when you want with BrellaTune Rentals &amp; Sales.</p>
      <p>We specialize in providing DJ entertainment without the DJ through unique touchscreen jukebox rentals for weddings, birthdays, graduation parties, corporate events, school events, class reunions, dances, and more.</p>
      <p>Our digital jukeboxes feature over 30,000 of the greatest hits of all time. Our touchscreen jukebox rentals are engineered to be interactive, fun, and easy to use. Your guests will be entertained all night long with music that is guaranteed to rock the party.</p>
    </div>
    <div class="tiles">
      <div class="tile light">
        <svg width="54" height="48" viewBox="0 0 54 48"><path d="M4 14h8v28h30v-8h6v14H4z" fill="#666"/><path d="M22 30c2-12 10-18 20-18V4l12 12-12 12v-8c-8 0-15 3-20 10z" fill="#666"/></svg>
        Rental<br>Request
      </div>
      <div class="tile dark">
        <svg width="60" height="56" viewBox="0 0 60 56"><path d="M6 26 30 2h24v24L30 50z" fill="none" stroke="#9aa0a8" stroke-width="3"/><circle cx="44" cy="12" r="4" fill="#9aa0a8"/></svg>
        Latest<br>Offers
      </div>
      <div class="tile enquiry dark-fill">
        BrellaTune<br>Enquiry
        <small>HOTLINE</small>
        <span class="value">+1 555 204 7710</span>
        <small>EMAIL</small>
        <span class="value">info@brellatune.com</span>
      </div>
      <div class="tile light">
        <svg width="44" height="56" viewBox="0 0 44 56"><path d="M2 54V22a20 20 0 0 1 40 0v32z" fill="none" stroke="#555" stroke-width="3"/><rect x="11" y="18" width="22" height="14" fill="#555"/><rect x="11" y="38" width="22" height="10" fill="none" stroke="#555" stroke-width="2"/></svg>
        Custom Made<br>Digital Jukebox
      </div>
    </div>
  </div>
</section>

<section class="featured">
  <div class="wrap">
    <h2 class="section-title lined">Featured <b>BrellaTune</b></h2>
    <div class="products">
      <article class="product">
        <div class="product-shot" role="img" aria-label="StageHub wall-mount jukebox"><span></span></div>
        <h3>StageHub Jukebox</h3>
        <p>The Cadenza Audio StageHub is the very latest online digital jukebox allowing.</p>
      </article>
      <article class="product">
        <div class="product-shot" role="img" aria-label="Touchscreen jukebox"><span></span></div>
        <h3>The Jukebox</h3>
        <p>The Cadenza Audio "The Jukebox" is the UK's highest earning digital jukebox.</p>
      </article>
      <article class="product">
        <div class="product-shot" role="img" aria-label="Digital jukebox cabinet"><span></span></div>
        <h3>Digital Jukebox</h3>
        <p>The Cadenza Audio StageHub is the very latest online digital jukebox allowing.</p>
      </article>
      <article class="product">
        <div class="product-shot" role="img" aria-label="RoomBox jukebox"><span></span></div>
        <h3>RoomBox Jukebox</h3>
        <p>The Cadenza Audio StageHub is the very latest online digital jukebox allowing.</p>
      </article>
    </div>
  </div>
</section>

<section class="best">
  <div class="wrap">
    <h2 class="section-title lined">Best of <b>BrellaTune</b></h2>
    <div class="best-cols">
      <div class="best-col feature-list">
        <h3>Imagine this…</h3>
        <ul>
          <li>30,000 of the greatest hit songs of all time</li>
          <li>Optional Digital Juke box Upgrade</li>
          <li>DJ Quality Lighting, Sound and Microphone</li>
          <li>User friendly Interface</li>
          <li>Customizable Playlist Builder</li>
          <li>Custom made Digital Jukebox for sale</li>
          <li>Free Delivery, Setup, Pickup and On-Call Service</li>
        </ul>
      </div>
      <div class="best-col custom-sale">
        <h3>Custom Made Digital<br>Juke Box Sale</h3>
        <p>Lorem ipsum dolor sit amet, consectetur adipiscing elit. Donec vehicula libero id ipsum finibus venenatis. Ut efficitur velit tincidunt. Nam suscipit ante egestas nisi eleifend, id maximus ante dapibus. Maecenas tempor.</p>
        <p>Urna vel velit venenatis tincidunt. Nulla nec nisl consequat at vulputate ac, pharetra eget nibh. Sed feugiat auctor velit a dapibus. Sed commodo eget felis sit amet tempor. Vivamus eget tristique nisi.</p>
      </div>
      <div class="best-col rental">
        <h3>Digital Jukeboxes<br>for Rental</h3>
        <p>Lorem ipsum dolor sit amet, consectetur adipiscing elit. Donec vehicula libero id ipsum finibus venenatis. Ut efficitur velit tincidunt. Nam suscipit ante egestas nisi eleifend, id maximus ante dapibus. Maecenas tempor.</p>
        <div class="check">Check availability &amp; get pricing</div>
        <div class="choose">Choose your date:</div>
        <div class="date-row"><span>Month</span><span>Day</span><span>Year</span></div>
        <span class="btn">Check Availability</span>
      </div>
    </div>
  </div>
</section>

<section class="contact">
  <div class="contact-map" role="img" aria-label="Street map showing the showroom location"></div>
  <div class="wrap">
    <h2>GET IN TOUCH</h2>
    <p class="lead">Have a question? do not hesitate to contact us.</p>
    <div class="info-boxes">
      <div class="info-box">
        <span class="badge"><svg width="14" height="18" viewBox="0 0 14 18"><path d="M7 0a7 7 0 0 1 7 7c0 5-7 11-7 11S0 12 0 7a7 7 0 0 1 7-7z" fill="#fff"/><circle cx="7" cy="7" r="2.5" fill="#e8692a"/></svg></span>
        <h4>Address</h4>
        <p>418 Larkspur Avenue, Port Elwin,<br>CA 90210</p>
      </div>
      <div class="info-box">
        <span class="badge"><svg width="16" height="16" viewBox="0 0 16 16"><path d="M3 1l3 0 1.5 4-2 1.5a9 9 0 0 0 4 4L11 8.5l4 1.5v3a2 2 0 0 1-2 2C6 15 1 10 1 3a2 2 0 0 1 2-2z" fill="#fff"/></svg></span>
        <h4>Phone</h4>
        <p>Local Support: 555 204 7711<br>Sales Department: 555 204 7712</p>
      </div>
      <div class="info-box">
        <span class="badge"><svg width="16" height="12" viewBox="0 0 16 12"><rect width="16" height="12" fill="#fff"/><path d="M0 0l8 7 8-7" fill="none" stroke="#e8692a" stroke-width="1.5"/></svg></span>
        <h4>Email us</h4>
        <p><a>support@brellatune.com</a></p>
      </div>
    </div>
    <div class="contact-form">
      <div class="form-row">
        <div class="field">Full Name</div>
        <div class="field">Email Address</div>
        <div class="field">Phone Number</div>
      </div>
      <div class="field message">Your message</div>
      <div class="form-foot">
        <span class="btn">Submit</span>
        <small>We will respond your message with 12 hours of working day</small>
      </div>
    </div>
  </div>
</section>

<footer class="site-footer">
  <div class="wrap footer-cols">
    <div class="footer-col"><h5>Information</h5><ul><li>About Us</li><li>Delivery Information</li><li>Privacy Policy</li><li>Terms &amp; Conditions</li></ul></div>
    <div class="footer-col"><h5>Customer Service</h5><ul><li>Contact Us</li><li>Returns</li><li>Site Map</li></ul></div>
    <div class="footer-col"><h5>Extras</h5><ul><li>Brands</li><li>Gift Vouchers</li><li>Affiliates</li><li>Specials</li></ul></div>
    <div class="footer-col"><h5>My Account</h5><ul><li>My Account</li><li>Order History</li><li>Wish List</li><li>Newsletter</li></ul></div>
  </div>
</footer>
<div class="footer-bar">
  <div class="wrap">
    <span>brellatune.com © 2015</span>
    <div class="footer-social"><span></span><span></span><span></span><span></span></div>
  </div>
</div>

</body>
</html>
```